BOX DESIGN OF CANINE AND FELINE RAPID TEST with PROFESSIONAL USE

"The market is in Southeast Asia, South America, Europe, and the U.S." Clients: Veterinary clinics, pet hospitals,(a small number of home use)
Positioned as a budget-friendly yet high-performance choice
Primary colors:
Green,Orange or Blue, (select 1,or 2 color)
Neutrals: Gray, Black or White (optional)
Dimensions:158mm(L)*98mm(W)*80mm(W)

Target Market(s)

Southeast Asia, South America, Europe, and the U.S.

Colors
0054AA
0677BA
7BADD7
CADEEF
E8F1F8
0094D4
00A9DD
6FCCEA
C7EBF8
E9F6FB
00AB8E
00BBA5
67D7C9
C6EFE9
E9F9F6
59FF00
82FF00
B8FF75
E3FFCB
F4FFEA
FFC000
F8CF3A
FAE287
FDF2CF
FEFAEE
F0912C
F2A743
F7CA91
FBE8D2
FDF5EE
EE7325
F08F49
F5BC92
FAE3D3
FDF4ED

Requirements
Nice to have
• Have an attractive look and preferably have pictures of pets (or outline lines of cats and dogs)

```html
<!DOCTYPE html>
<html lang="en">
<head>
<meta charset="utf-8">
<title>Vetra Scan – Canine &amp; Feline Rapid Test Kit Dieline</title>
<link href="https://fonts.googleapis.com/css2?family=Barlow+Condensed:ital,wght@0,400;0,500;0,700;1,300;1,400;1,500;1,700&family=Montserrat:wght@500;700&display=swap" rel="stylesheet">
<style>
  :root{
    --blue-deep:#0054AA;
    --blue:#0677BA;
    --blue-bright:#0094D4;
    --cyan:#00A9DD;
    --sky:#6FCCEA;
    --ice:#E9F6FB;
    --paper:#F6F7F8;
    --ink:#1A1A1A;
    --cut:#222;
    --shade:#C9CDD1;
    --seal:#D5DAE0;
  }
  *{box-sizing:border-box;margin:0;padding:0}
  html,body{width:1200px;height:722px;overflow:hidden;background:#fff}
  .dieline{position:relative;width:1200px;height:722px;font-family:"Barlow Condensed",sans-serif;color:#fff}
  .dieline svg.shapes{position:absolute;inset:0}
  .t{position:absolute;white-space:nowrap;line-height:1}
  .it{font-style:italic}
  .brand{font-family:"Barlow Condensed",sans-serif;font-weight:500;font-style:normal;letter-spacing:.5px;color:var(--blue-bright);display:flex;align-items:center;gap:6px}
  .brand .dot{width:.55em;height:.55em;border-radius:50%;background:var(--blue-bright)}
  .brand.light{color:#fff}
  .brand.light .dot{background:#fff}
  .tagline{font-family:"Montserrat",sans-serif;font-weight:500;color:var(--ink);letter-spacing:.4px}
  .tagline.light{color:#fff}
  .title-dark{color:var(--ink);font-style:italic;font-weight:300;text-align:center}
  .pill{position:absolute;border:1px solid rgba(255,255,255,.35);background:rgba(255,255,255,.12);border-radius:3px;display:flex;align-items:center;justify-content:center;font-style:italic;font-weight:400}
  .kit-list{list-style:none}
  .kit-list li{font-style:italic;font-weight:400;font-size:8.5px;line-height:10.5px;display:flex;align-items:center;gap:6px}
  .kit-list li::before{content:"";width:3px;height:3px;border-radius:50%;background:#fff}
  .feature h4{font-style:italic;font-weight:500;font-size:6.5px;line-height:7px}
  .feature p{font-style:italic;font-weight:400;font-size:3.4px;line-height:4px;opacity:.9}
  .tile{position:absolute;width:58px;height:58px;border:1.5px solid #fff;border-radius:3px;background:linear-gradient(180deg,var(--cyan),var(--blue));display:flex;flex-direction:column;align-items:center;padding-top:8px}
  .tile .rule{width:46px;height:1px;background:rgba(255,255,255,.6);margin:6px 0 3px}
  .tile strong{font-style:italic;font-weight:700;font-size:9px;line-height:9px}
  .tile small{font-style:italic;font-size:3.6px;line-height:5px}
  .photo{position:absolute;border-radius:6px}
</style>
</head>
<body>
<div class="dieline">
  <svg class="shapes" width="1200" height="722" viewBox="0 0 1200 722">
    <defs>
      <linearGradient id="blueFill" x1="0" y1="0" x2="1" y2="0">
        <stop offset="0" stop-color="#1A6FC0"/>
        <stop offset=".6" stop-color="#0677BA"/>
        <stop offset="1" stop-color="#00A9DD"/>
      </linearGradient>
      <linearGradient id="blueBand" x1="0" y1="0" x2="1" y2="0">
        <stop offset="0" stop-color="#0677BA"/>
        <stop offset="1" stop-color="#00A9DD"/>
      </linearGradient>
    </defs>
    <g fill="url(#blueFill)">
      <path d="M92,485 H428 V634 H372 Q342,634 342,606 V582 H182 V606 Q182,634 152,634 H92 Z"/>
      <path d="M417,485 H611 V603 H528 Q502,603 502,578 V552 L428,505 Z"/>
      <path d="M611,485 H922 L866,571 V605 Q866,630 840,630 H694 Q668,630 668,605 V571 Z"/>
      <path d="M922,485 H1125 V495 L1032,558 V604 H906 V485 Z"/>
      <path d="M421,327 V238 Q421,230 430,230 H588 Q606,230 609,252 L620,327 Z"/>
      <path d="M912,327 L921,256 Q925,232 950,232 H1125 V327 Z"/>
      <rect x="100" y="228" width="322" height="99" fill="url(#blueBand)"/>
      <rect x="56" y="438" width="1069" height="47"/>
      <rect x="417" y="327" width="194" height="158"/>
      <rect x="922" y="327" width="203" height="158"/>
    </g>
    <rect x="100" y="88" width="322" height="140" fill="var(--paper)"/>
    <path d="M106,134 V114 Q106,94 126,94 H397 Q417,94 417,114 V134" fill="#fff" stroke="var(--cut)" stroke-width=".8"/>
    <rect x="106" y="134" width="311" height="90" fill="#fff"/>
    <rect x="100" y="224" width="322" height="4" fill="var(--shade)"/>
    <polygon points="56,332 106,327 106,438 56,438" fill="var(--paper)"/>
    <rect x="106" y="327" width="311" height="109" fill="#fff"/>
    <rect x="106" y="436" width="311" height="3" fill="var(--shade)"/>
    <rect x="611" y="327" width="311" height="109" fill="#fff"/>
    <rect x="611" y="434" width="311" height="3" fill="var(--shade)"/>
    <g fill="none" stroke="var(--cut)" stroke-width=".7">
      <line x1="106" y1="134" x2="417" y2="134"/>
      <line x1="66" y1="327" x2="1116" y2="327"/>
      <line x1="66" y1="485" x2="1116" y2="485"/>
      <polyline points="106,327 66,334 66,481 106,485"/>
      <line x1="106" y1="134" x2="106" y2="620"/>
      <line x1="417" y1="134" x2="417" y2="620"/>
      <line x1="611" y1="327" x2="611" y2="592"/>
      <line x1="922" y1="327" x2="922" y2="592"/>
      <line x1="1116" y1="327" x2="1116" y2="485"/>
      <path d="M106,620 H160 Q172,620 172,606 V592 H350 V606 Q350,620 362,620 H417"/>
      <path d="M417,485 L514,553 V578 Q514,592 530,592 H611"/>
      <path d="M611,485 L678,571 V607 Q678,620 692,620 H842 Q855,620 855,607 V571 L922,485"/>
      <path d="M922,592 H1005 Q1020,592 1020,578 V552 L1116,485"/>
      <path d="M421,327 V238 H590 Q600,238 602,252 L610,322 L611,327"/>
      <path d="M922,327 L930,250 Q934,239 948,239 H1111 V322 L1116,327"/>
    </g>
  </svg>

  <!-- TOP PANEL -->
  <div class="t brand" style="left:222px;top:157px;font-size:24px">VETRA SCAN</div>
  <div class="t tagline" style="left:224px;top:181px;font-size:5px">CLEAR ANSWERS FOR EVERY PAW</div>
  <div class="t" style="left:346px;top:139px;width:62px;height:26px;border:1px solid #e3e5e7;border-radius:3px;color:var(--ink);font-style:italic;font-weight:700;display:flex;align-items:center;justify-content:center;gap:2px"><span style="font-size:13px">10</span><span style="font-size:8px">TESTS/BOX</span></div>
  <div class="t title-dark" style="left:106px;width:311px;top:195px;font-size:22px">CANINE &amp; FELINE RAPID TEST KIT</div>

  <div class="t it" style="left:132px;top:246px;font-size:14px;font-weight:700">KIT CONTENTS</div>
  <ul class="t kit-list" style="left:133px;top:266px">
    <li>TEST KITS</li><li>ASSAY BUFFER</li><li>STERILE SWABS</li><li>INSTRUCTION MANUAL</li>
  </ul>
  <div class="t" style="left:260px;top:271px;width:137px;height:47px;border:1px solid rgba(255,255,255,.3);background:rgba(255,255,255,.1);border-radius:3px"></div>
  <svg class="t" style="left:270px;top:278px" width="120" height="20" viewBox="0 0 120 20" fill="none" stroke="#fff" stroke-width="1">
    <rect x="1" y="5" width="17" height="10"/><text x="3.5" y="13" fill="#fff" stroke="none" font-size="7" font-family="Montserrat" font-weight="700">IDV</text>
    <line x1="37" y1="3" x2="37" y2="14"/><circle cx="37" cy="16" r="2.5"/><path d="M30,17 L44,3"/>
    <circle cx="62" cy="9" r="3"/><path d="M62,1 V4 M62,14 V17 M54,9 H57 M67,9 H70 M56,3 L58,5 M66,13 L68,15 M68,3 L66,5 M56,15 L58,13"/>
    <path d="M78,5 Q83,3 87,5 V16 Q83,14 78,16 Z M87,5 Q91,3 96,5 V16 Q91,14 87,16"/><line x1="91" y1="9" x2="91" y2="13"/>
    <circle cx="108" cy="10" r="6"/><path d="M104,6 L112,14 M112,6 L104,14"/>
  </svg>
  <div class="t it" style="left:265px;top:305px;font-size:8px">STORE AT 2-30°C &nbsp; - &nbsp; AVOID DIRECT SUNLIGHT</div>

  <!-- FRONT PANEL -->
  <div class="photo" role="img" aria-label="Photo of a dog with three kittens" style="left:106px;top:348px;width:132px;height:102px;background:radial-gradient(ellipse at 50% 45%,#C98A4E,#8E5A34 55%,rgba(255,255,255,0) 78%)"></div>
  <div class="t brand" style="left:262px;top:338px;font-size:25px">VETRA SCAN</div>
  <div class="t tagline" style="left:274px;top:363px;font-size:5px">CLEAR ANSWERS FOR EVERY PAW</div>
  <div class="t title-dark" style="left:238px;width:140px;top:380px;font-size:25px;line-height:21px;white-space:normal">CANINE &amp; FELINE RAPID TEST KIT</div>
  <div class="pill" style="left:295px;top:444px;width:111px;height:17px;font-size:8px">VETERINARIAN RECOMMENDED</div>
  <div class="pill" style="left:295px;top:462px;width:111px;height:15px;font-size:6px;background:none">DIGITAL RESULTS IN &lt; 10 MINUTES</div>

  <!-- SIDE PANEL 1 -->
  <div class="t it" style="left:437px;top:340px;font-size:11px">VETRA SCAN RAPID TEST</div>
  <div class="t" style="left:432px;top:358px;width:80px">
    <div class="feature"><h4>SIMPLE CONVENIENT</h4><p>NO SPECIAL SKILLS NEEDED, EASY ENOUGH FOR HOME USE.</p></div>
    <div class="feature" style="margin-top:5px"><h4>ACCURATE RELIABLE</h4><p>CLEAR RESULTS FROM LATERAL FLOW TESTING, TRUSTED BY CLINICS.</p></div>
    <div class="feature" style="margin-top:5px"><h4>FAST EFFICIENT</h4><p>RESULTS IN UNDER 10 MINUTES FROM START TO END.</p></div>
  </div>
  <div class="photo" role="img" aria-label="Photo of a dog and a cat sitting together" style="left:514px;top:356px;width:78px;height:84px;background:linear-gradient(160deg,#B07A45,#6E5240 60%,#8C8478)"></div>
  <div class="t" style="left:432px;top:419px;width:80px;height:21px;background:rgba(255,255,255,.14);border-radius:2px;font-style:italic;font-size:3.6px;line-height:4.5px;text-align:center;padding-top:5px;white-space:normal">SCREENS FOR SEVERAL DISEASES, HELPING OWNERS SPOT ISSUES EARLY.</div>
  <div class="t" style="left:432px;top:448px;width:161px;height:29px;border:1px solid rgba(255,255,255,.3);background:rgba(255,255,255,.08);border-radius:3px"></div>
  <div class="t it" style="left:441px;top:454px;font-size:3.5px">MADE BY</div>
  <div class="t it" style="left:440px;top:459px;font-size:8px;font-weight:500">NORVELLE LABS</div>
  <div class="t it" style="left:440px;top:468px;font-size:3.5px">CLEAR ANSWERS FOR EVERY PAW</div>
  <div class="t brand light" style="left:541px;top:459px;font-size:8px;gap:3px"><span class="dot"></span>VETRA SCAN</div>

  <!-- BACK PANEL -->
  <div class="t brand" style="left:682px;top:348px;font-size:32px">VETRA SCAN</div>
  <div class="t tagline" style="left:684px;top:381px;font-size:6px">CLEAR ANSWERS FOR EVERY PAW</div>
  <div class="t" style="left:838px;top:334px;width:62px;height:97px;border:1px solid #e6e8ea;border-radius:4px;background:#f7f8f9"></div>
  <div class="t" style="left:854px;top:344px;width:30px;height:30px;border-radius:50%;background:var(--seal)"></div>
  <div class="t" style="left:844px;top:384px;width:50px;height:1px;background:#dde0e3"></div>
  <div class="t" style="left:852px;top:393px;width:34px;height:34px;border-radius:50%;background:var(--seal)"></div>

  <div class="tile" style="left:629px;top:403px">
    <svg width="20" height="20" viewBox="0 0 20 20" fill="none" stroke="#fff" stroke-width="1.8"><path d="M17,10 A7,7 0 1 1 13,3.6"/><path d="M10,5.5 V10 L13,12"/><path d="M13,1 L13.5,4 L10.5,4.5"/></svg>
    <div class="rule"></div><strong>RESULTS IN</strong><small>10 MIN</small>
  </div>
  <div class="tile" style="left:694px;top:403px">
    <svg width="20" height="20" viewBox="0 0 20 20" fill="none" stroke="#fff" stroke-width="1.6"><circle cx="10" cy="10" r="8"/><path d="M10,2 V18 M6,6 Q10,10 6,14 M14,6 Q10,10 14,14"/></svg>
    <div class="rule"></div><strong>HEALTH CHECK</strong><small>FOR DOG AND CAT</small>
  </div>
  <div class="tile" style="left:756px;top:403px">
    <svg width="20" height="20" viewBox="0 0 20 20" fill="none" stroke="#fff" stroke-width="1.8"><circle cx="10" cy="10" r="8"/><path d="M6,10 L9,13 L15,6"/></svg>
    <div class="rule"></div><strong>EASY</strong><small>TO USE</small>
  </div>

  <!-- SIDE PANEL 2 -->
  <div class="t brand light" style="left:998px;top:340px;font-size:14px">VETRA SCAN</div>
  <div class="t tagline light" style="left:1000px;top:355px;font-size:3px">CLEAR ANSWERS FOR EVERY PAW</div>
  <svg class="t" style="left:933px;top:368px" width="164" height="61" viewBox="0 0 164 61" fill="none" stroke="#fff" stroke-width="1.4">
    <path d="M1,7 V1 H7 M157,1 H163 V7 M1,54 V60 H7 M157,60 H163 V54"/>
  </svg>
  <div class="t" style="left:1058px;top:441px;width:15px;height:15px;border-radius:50%;background:#fff"></div>
  <div class="t" style="left:1082px;top:441px;width:13px;height:15px;background:#fff"></div>
  <div class="t" style="left:1058px;top:462px;width:15px;height:15px;border-radius:50%;background:#fff"></div>
  <div class="t" style="left:1082px;top:462px;width:13px;height:15px;background:#fff"></div>
</div>
</body>
</html>
```